Web page design for technology solution company
Velmork Inc.
Dear PH,
Kindly star rate #83 it will help me to go through.
Thanks!
Hi PH,
Any feedback for #52
Thanks
Kindly check your private messages.
#57 and #58 - don't need the extra info. Stick with your earlier versions - like those better. They're simple and not 'overloaded'
#55, #56 - like the simplicity but don't like the dark background
Hi PH, please check your private message. thanks
#13 and #19 - can we see the design without the graphics?
#20 -#24 - much better with the lighter background!
@PH
Kindly check your private message box on the top right & reply asap with your feedback.Thanks
#10 - #12. They seem interesting but on the darker side. Can we see them with a white background?
#9 - Nice and clean design. It's unique and colors are nicely coordinated. Can you find a place for social media icons?
#1 - #5 . Some of the designs look interesting but the background is too dark. Can we see the same with white background?
PH please check your private message
Perin Koldesh

```html
<!DOCTYPE html>
<html lang="en">
<head>
<meta charset="utf-8">
<title>Velmork Inc.</title>
<link href="https://fonts.googleapis.com/css2?family=Oswald:wght@400;500&family=Open+Sans:wght@400&display=swap" rel="stylesheet">
<style>
  :root {
    --page-bg: #f1f1f1;
    --swoosh-lime: #b6e21a;
    --swoosh-grey: #c9c9c9;
    --lime-top: #d9f24a;
    --lime-bottom: #a9cf14;
    --tile-top: #d6d6d6;
    --tile-bottom: #7b7b7b;
    --tile-label: #ffffff;
    --icon-dark: #3a3a3a;
    --text-dark: #3d3d3d;
    --text-soft: #6a6a6a;
    --logo-grey: #7a7a7a;
    --footer-bg: #e6e6e6;
    --footer-line: #d0d0d0;
    --footer-text: #9a9a9a;
    --social-grey: #a8a8a8;
  }
  * { margin: 0; padding: 0; box-sizing: border-box; }
  html, body { width: 1200px; height: 588px; overflow: hidden; }
  body {
    position: relative;
    background: var(--page-bg);
    font-family: "Open Sans", Arial, sans-serif;
  }
  .backdrop {
    position: absolute; inset: 0;
    background:
      radial-gradient(ellipse 420px 90px at 960px 150px, rgba(182,226,26,.55), transparent 70%),
      radial-gradient(ellipse 380px 70px at 200px 440px, rgba(182,226,26,.45), transparent 70%),
      radial-gradient(ellipse 700px 160px at 600px 300px, rgba(255,255,255,.9), transparent 70%),
      linear-gradient(160deg, #ffffff 0%, #e9e9e9 35%, #f7f7f7 55%, #dcdcdc 80%, #f4f4f4 100%);
  }
  .swoosh { position: absolute; inset: 0; }
  .brand {
    position: absolute; top: 52px; left: 0; width: 100%;
    display: flex; justify-content: center; align-items: center; gap: 14px;
  }
  .brand-dot {
    width: 44px; height: 44px; border-radius: 50%;
    background: var(--logo-grey);
  }
  .brand-name {
    font-family: "Oswald", Arial, sans-serif; font-weight: 400;
    font-size: 50px; color: var(--logo-grey); line-height: 1;
  }
  .nav-tiles {
    position: absolute; top: 163px; left: 269px;
    display: flex; gap: 55px;
  }
  .tile {
    width: 187px; height: 216px; border-radius: 4px;
    background: linear-gradient(180deg, var(--tile-top), var(--tile-bottom));
    box-shadow: 0 18px 22px -10px rgba(0,0,0,.35);
    display: flex; flex-direction: column; align-items: center;
    text-decoration: none;
  }
  .tile--active { background: linear-gradient(180deg, var(--lime-top), var(--lime-bottom)); }
  .tile-icon { margin-top: 38px; width: 84px; height: 100px; display: flex; align-items: center; justify-content: center; }
  .person-slot {
    width: 70px; height: 96px; border-radius: 35px 35px 10px 10px;
    background: linear-gradient(180deg, #5a5a5a, #2c2c2c);
  }
  .tile-label {
    margin-top: 14px;
    font-family: "Oswald", Arial, sans-serif; font-weight: 500;
    font-size: 21px; letter-spacing: .5px; color: var(--tile-label);
    text-transform: uppercase;
  }
  .tagline {
    position: absolute; top: 424px; width: 100%; text-align: center;
  }
  .tagline-main { font-size: 26px; color: var(--text-dark); }
  .tagline-sub { font-size: 13px; color: var(--text-soft); margin-top: 2px; }
  .site-footer {
    position: absolute; left: 0; bottom: 0; width: 100%; height: 56px;
    background: var(--footer-bg); border-top: 1px solid var(--footer-line);
  }
  .footer-brand {
    position: absolute; left: 200px; top: 15px;
    display: flex; align-items: center; gap: 8px;
  }
  .footer-dot { width: 20px; height: 20px; border-radius: 50%; background: var(--footer-text); }
  .footer-name { font-family: "Oswald", Arial, sans-serif; font-size: 20px; color: var(--footer-text); line-height: 1; }
  .copyright {
    position: absolute; top: 20px; width: 100%; text-align: center;
    font-size: 10px; color: var(--footer-text);
  }
  .social-links {
    position: absolute; right: 204px; top: 14px; display: flex; gap: 10px;
  }
  .social-links span {
    width: 28px; height: 28px; border-radius: 50%; background: var(--social-grey); display: block;
  }
</style>
</head>
<body>
  <div class="backdrop"></div>
  <svg class="swoosh" width="1200" height="588" viewBox="0 0 1200 588" aria-hidden="true">
    <path d="M640 250 C820 180 1000 110 1200 40 L1200 120 C1010 170 830 220 640 250 Z" fill="var(--swoosh-lime)" opacity=".35"/>
    <path d="M0 470 C160 430 330 410 520 400 C330 430 160 460 0 500 Z" fill="var(--swoosh-lime)" opacity=".35"/>
    <path d="M0 250 C300 330 700 360 1200 300 L1200 330 C700 390 300 360 0 290 Z" fill="var(--swoosh-grey)" opacity=".25"/>
  </svg>

  <header class="brand">
    <span class="brand-dot"></span>
    <span class="brand-name">Velmork Inc.</span>
  </header>

  <nav class="nav-tiles">
    <a class="tile tile--active" href="#about">
      <div class="tile-icon"><div class="person-slot" role="img" aria-label="Dark figure silhouette icon"></div></div>
      <span class="tile-label">About Us</span>
    </a>
    <a class="tile" href="#products">
      <div class="tile-icon">
        <svg width="84" height="70" viewBox="0 0 84 70" aria-hidden="true">
          <path d="M4 10 h26 l6 7 h44 v49 h-76 Z" fill="var(--icon-dark)"/>
          <rect x="30" y="22" width="24" height="40" rx="4" fill="#1f1f1f" stroke="#777" stroke-width="2"/>
        </svg>
      </div>
      <span class="tile-label">Products</span>
    </a>
    <a class="tile" href="#contact">
      <div class="tile-icon">
        <svg width="86" height="72" viewBox="0 0 86 72" aria-hidden="true">
          <path d="M30 4 h48 a6 6 0 0 1 6 6 v26 a6 6 0 0 1 -6 6 h-6 l4 12 -16 -12 h-30 a6 6 0 0 1 -6 -6 v-26 a6 6 0 0 1 6 -6 Z" fill="#555"/>
          <path d="M6 22 h44 a6 6 0 0 1 6 6 v22 a6 6 0 0 1 -6 6 h-26 l-14 12 3 -12 h-7 a6 6 0 0 1 -6 -6 v-22 a6 6 0 0 1 6 -6 Z" fill="var(--icon-dark)"/>
        </svg>
      </div>
      <span class="tile-label">Contact</span>
    </a>
  </nav>

  <section class="tagline">
    <p class="tagline-main">We provide branded online and mobile platforms and service solutions</p>
    <p class="tagline-sub">that enable and enhance eCommerce and other online interactions for individuals and businesses.</p>
  </section>

  <footer class="site-footer">
    <div class="footer-brand"><span class="footer-dot"></span><span class="footer-name">Velmork Inc.</span></div>
    <p class="copyright">Copyright © 2013 Velmork Inc. All Rights Reserved</p>
    <div class="social-links"><span></span><span></span><span></span></div>
  </footer>
</body>
</html>
```